Kindle Your Patrons Book Cover

A book main title will be, "Kindle Your Patrons"
The subtext will be, "Go to market with a story that sizzles"
Would like it to blend with my web site brand. You can find it here: www.kindleyourpatrons.example

Audience is business and revenue leaders for small, medium and large businesses. They have a new solution, or want to enter a new market, and they need to "kindle their patrons" meaning getting the buyers to want to change enough to overcome their status quo bias. They need a story that sizzles to do this.

```html
<!DOCTYPE html>
<html lang="en">
<head>
<meta charset="utf-8">
<title>Kindle Your Patrons — Book Cover</title>
<link href="https://fonts.googleapis.com/css2?family=Anton&family=Bebas+Neue&family=Syncopate:wght@700&display=swap" rel="stylesheet">
<style>
  :root {
    --teal: #00a8aa;
    --ink: #03242b;
    --sub-teal: #1a9e91;
    --mark-slate: #34465e;
    --paper: #f7fbfb;
    --mist: #d6eeee;
  }
  html, body {
    margin: 0;
    padding: 0;
    width: 768px;
    height: 1200px;
    overflow: hidden;
    background: var(--paper);
  }
  .cover {
    position: relative;
    width: 768px;
    height: 1200px;
    overflow: hidden;
    background: var(--paper);
  }
  .cover-backdrop {
    position: absolute;
    inset: 0;
    background:
      linear-gradient(180deg, rgba(160, 215, 218, 0.85) 0%, rgba(210, 236, 237, 0.7) 22%, rgba(244, 250, 250, 0.6) 45%, rgba(250, 252, 252, 0.9) 64%, rgba(236, 246, 246, 1) 100%),
      linear-gradient(90deg, #9fd3d6 0%, #e9f5f5 30%, #f3f9f9 60%, #d9eeee 100%);
  }
  .cover-art {
    position: absolute;
    inset: 0;
    width: 768px;
    height: 1200px;
  }
  .imprint-name {
    font-family: "Syncopate", sans-serif;
    font-weight: 700;
    fill: var(--ink);
  }
  .imprint-dot { fill: var(--teal); }
  .title-main {
    font-family: "Anton", sans-serif;
    fill: var(--teal);
  }
  .title-second {
    font-family: "Anton", sans-serif;
    fill: var(--ink);
  }
  .trademark {
    font-family: "Anton", sans-serif;
    fill: var(--mark-slate);
  }
  .subtitle {
    font-family: "Syncopate", sans-serif;
    font-weight: 700;
    fill: var(--sub-teal);
  }
  .author {
    font-family: "Bebas Neue", sans-serif;
    fill: var(--teal);
  }
</style>
</head>
<body>
  <main class="cover">
    <div class="cover-backdrop" role="img" aria-label="Soft, faded photograph of glass office towers overlaid with thin white network lines"></div>
    <svg class="cover-art" viewBox="0 0 768 1200" xmlns="http://www.w3.org/2000/svg">
      <g class="imprint">
        <circle class="imprint-dot" cx="319" cy="61" r="6"/>
        <text class="imprint-name" x="332" y="67" font-size="16">EMBERLINE</text>
      </g>

      <text class="title-main" x="38" y="469" font-size="272" textLength="694" lengthAdjust="spacingAndGlyphs">KINDLE</text>
      <text class="trademark" x="684" y="516" font-size="32" textLength="48" lengthAdjust="spacingAndGlyphs">TM</text>
      <text class="title-second" x="40" y="642" font-size="156" textLength="690" lengthAdjust="spacingAndGlyphs">YOUR PATRONS</text>

      <text class="subtitle" x="103" y="737" font-size="36" textLength="564" lengthAdjust="spacingAndGlyphs">GO TO MARKET WITH</text>
      <text class="subtitle" x="65" y="788" font-size="36" textLength="641" lengthAdjust="spacingAndGlyphs">A STORY THAT SIZZLES</text>

      <text class="author" x="38" y="1163" font-size="116" textLength="694" lengthAdjust="spacing">DANA WHITCOMB</text>
    </svg>
  </main>
</body>
</html>
```